Family Farm Business Requires Flyer for local CSA retail sales and local advertising

We need a flyer design for our small farm to help promote our CSA business. A CSA is when someone pre-pays for a summer's worth of produce, fruit, and eggs that are raised on our farm. They receive a weekly box of produce and essentially they buy a small share of the summer's bounty. We had a logo designed by someone here on pixel hive so we would like the flyer to include the colors of the logo. The final design should reflect the different options for people the choose and then invite them to sign up to be a CSA Customer.

Target Market(s)

Busy families and moms who are limited in time to buy groceries or healthy food or produce. People who are passionate about local food and local produce.

Industry/Entity Type

Advertising

Font styles to use
Decorative
Script

Requirements
Must have
• Our logo, our farm information (website, social media, location) and contact info as well as the various options to choose from for our CSA farm share. I also included a picture of our business card so it would be good if it matched the colors/style of our card. Also the flyer will be printed on 8.5 x 11 paper and it will be double sided.

```html
<!DOCTYPE html>
<html lang="en">
<head>
<meta charset="utf-8">
<title>Maple Hollow Farm – Summer CSA</title>
<link href="https://fonts.googleapis.com/css2?family=Amatic+SC:wght@400;700&family=Encode+Sans+Condensed:wght@400;500;700&display=swap" rel="stylesheet">
<style>
  :root{
    --green-dark:#1b8a4b;
    --green-mid:#2f9a46;
    --green-light:#8dc63f;
    --green-pale:#a6cf63;
    --panel:#eef5e2;
    --card:#cfe5d0;
    --fruit:#a9d46b;
    --egg:#f6e39b;
    --yellow:#f4b71b;
    --ink:#1c1c1c;
    --grey:#6b6b6b;
    --hand:"Amatic SC", cursive;
    --sans:"Encode Sans Condensed", sans-serif;
  }
  *{box-sizing:border-box;margin:0;padding:0}
  html,body{width:927px;height:1200px;overflow:hidden;background:#fff}
  body{position:relative;font-family:var(--sans);color:var(--ink)}
  .abs{position:absolute}

  .panel{left:48px;top:68px;width:792px;height:667px;background:var(--panel);border-radius:52px}

  .brand{left:72px;top:42px;width:140px;height:170px;display:flex;flex-direction:column;align-items:center;justify-content:center;gap:10px}
  .brand-dot{width:36px;height:36px;border-radius:50%;background:var(--yellow)}
  .brand-name{font-family:var(--sans);font-weight:700;color:var(--green-dark);font-size:24px;line-height:1.05;text-align:center;text-transform:uppercase}

  .tagline{left:56px;top:240px;width:164px;text-align:center;font-family:var(--hand);color:var(--green-pale);font-size:38px;line-height:35.5px;white-space:nowrap}

  .pickup{left:50px;top:482px;width:176px;text-align:center}
  .pickup h3{font-family:var(--sans);font-weight:500;color:var(--green-dark);font-size:17px;line-height:21px;text-transform:uppercase;margin-bottom:10px}
  .pickup .day{font-family:var(--hand);color:var(--green-light);font-size:19px;line-height:20px}
  .pickup .place{font-size:11.5px;line-height:16px;margin-bottom:8px}
  .pickup .opt{font-family:var(--hand);font-size:14px;font-weight:700}

  .section-label{font-family:var(--sans);font-weight:700;font-size:24px;text-transform:uppercase}
  .produce-label{left:235px;top:82px;color:var(--green-dark)}
  .eggs-label{left:235px;top:502px;color:var(--yellow)}
  .fruit-label{left:742px;top:502px;color:var(--green-light)}

  .month{top:140px;width:135px;height:235px;background:var(--card);border-radius:28px;padding:12px 2px;text-align:center}
  .month h2{font-family:var(--hand);font-weight:400;font-size:46px;line-height:52px;color:#2a2a2a;margin-bottom:6px;white-space:nowrap}
  .month h2 small{font-size:11px;display:inline-block;line-height:10px;vertical-align:16px}
  .month p{font-size:12px;line-height:18.2px;color:var(--green-mid);font-weight:500;letter-spacing:-0.2px}
  .month p .soft{color:var(--grey);font-weight:400}

  .pill{top:387px;width:135px;height:70px;border-radius:22px;display:flex;align-items:center;justify-content:center;text-align:center;font-size:12.5px;line-height:16px}
  .pill.egg{background:var(--egg)}
  .pill.fruit{background:var(--fruit)}

  .goal{left:236px;top:547px;width:580px;font-size:15.4px;line-height:22px;letter-spacing:-0.1px}
  .notes{left:236px;top:600px;width:572px;display:grid;grid-template-columns:repeat(3,1fr);gap:14px}
  .notes p{font-size:11.5px;line-height:17px;color:var(--green-pale);text-align:justify}

  .order-title{left:48px;top:754px;font-size:11px;font-weight:500}
  .field{left:48px;width:292px;border-top:1px solid #555;font-family:var(--hand);font-size:10px;padding-top:2px}
  .field span{display:inline-block}

  .shares{left:362px;top:753px;width:185px}
  .shares h4,.pref h4{font-size:11px;font-weight:500;text-align:center;margin-bottom:2px}
  .shares .sub{font-size:7.5px;font-style:italic;text-align:center;color:#444;line-height:10px;margin-bottom:10px}
  .check{display:flex;align-items:center;gap:6px;font-size:12px;margin-bottom:6px;white-space:nowrap}
  .check i{width:13px;height:13px;border:1.3px solid #333;border-radius:50%;flex:none}
  .check i.sm{width:9px;height:9px}
  .check b{font-family:var(--hand);font-weight:400;font-size:17px}
  .indent{font-size:11px}

  .pref{left:558px;top:753px;width:330px}
  .pref h4{text-align:left;margin-bottom:8px}
  .pref .check{font-size:11px;margin-bottom:4px}
  .pref .circle{font-size:8px;font-style:italic;margin-left:22px}
  .pref .circle b{font-family:var(--hand);font-size:16px;font-style:normal;font-weight:400}

  .terms{left:48px;top:998px;width:625px;font-size:9.6px;line-height:12.6px;color:#333}
  .terms h5{font-size:10px;font-weight:700;color:var(--ink)}
  .terms strong{color:var(--ink)}

  .mail{left:691px;top:1010px;width:200px;font-size:11px;line-height:16px}
  .mail em{font-weight:700}
</style>
</head>
<body>
  <div class="abs panel"></div>

  <div class="abs brand">
    <div class="brand-dot"></div>
    <div class="brand-name">Maple Hollow<br>Farm</div>
  </div>

  <div class="abs tagline">Examples<br>of what to<br>expect in<br>your share<br>every<br>month</div>

  <div class="abs pickup">
    <h3>Pick-up<br>dates &amp; locations</h3>
    <div class="day">Tuesday</div>
    <div class="place">at Maple Hollow Farm</div>
    <div class="day">Tuesday Afternoon</div>
    <div class="place">at Cedar Grove Community<br>Church, Millbrook</div>
    <div class="day">Saturdays</div>
    <div class="place">at Riverside Farmers Market<br><span class="opt">Pre-picked</span> or <span class="opt">Market Shopper</span></div>
  </div>

  <div class="abs section-label produce-label">Produce</div>

  <svg class="abs" style="left:218px;top:112px" width="624" height="390" viewBox="0 0 624 390" aria-hidden="true">
    <path d="M6 36 Q6 8 36 8 H590 Q618 8 618 36" fill="none" stroke="var(--green-dark)" stroke-width="8"/>
    <path d="M6 300 V342 Q6 374 38 374 H588 Q618 374 618 342 V300" fill="none" stroke="var(--yellow)" stroke-width="7"/>
    <path d="M156 330 V346 Q156 362 174 362 H590 Q610 362 610 344 V330" fill="none" stroke="var(--green-light)" stroke-width="7"/>
  </svg>

  <div class="abs month" style="left:230px">
    <h2>June</h2>
    <p>Broccoli, Cabbage, Sugar Snap Peas, Various Lettuces, Spinach, Kale, Swiss Chard, Beets</p>
  </div>
  <div class="abs month" style="left:377px">
    <h2>July</h2>
    <p>Broccoli, Lettuces, Kale,<br>Snow Peas, Summer<br>Squash, Zucchini,<br>Cucumbers, Slicing<br>Tomatoes, Cherry<br>Tomatoes, Green Beans,<br>October Beans,<br>White &amp; Yellow Corn</p>
  </div>
  <div class="abs month" style="left:523px">
    <h2>August</h2>
    <p><span class="soft">Same as July also -</span><br>Various Bell Peppers,<br>Sweet Peppers,<br>Hot Peppers,<br>Sweet onions</p>
  </div>
  <div class="abs month" style="left:669px">
    <h2>Sept<small>thru<br>mid</small>Oct</h2>
    <p><span class="soft">Much the same as<br>July/August<br>along with -</span><br>several different<br>varieties of potatoes<br>along with a few<br>surprises</p>
  </div>

  <div class="abs pill egg" style="left:230px">1 Dozen<br>Large Brown Eggs<br>weekly for 20 weeks</div>
  <div class="abs pill fruit" style="left:377px">Peaches, Pears, &amp;<br>Blackberries</div>
  <div class="abs pill fruit" style="left:523px">Peaches, Pears, &amp;<br>Blackberries</div>
  <div class="abs pill fruit" style="left:669px">Eating &amp;<br>Cooking Apples</div>

  <div class="abs section-label eggs-label">Eggs</div>
  <div class="abs section-label fruit-label">Fruit</div>

  <p class="abs goal">Our goal is a sustainable farm and land that uses crop rotation and cover crops to build and amend<br>the soil and provide the best quality produce and fruit in this area.</p>

  <div class="abs notes">
    <p>We are planning on an 18 week share that begins in June and will run to mid-October. Because of our climate and temps the summer stock will start coming in early to mid July and run through August.</p>
    <p>We are committed to planting non-GMO seed as well as planting many heirloom varieties of seed to keep the past alive and bring back tastes and flavors from the past.</p>
    <p>Our eggs are truly free range, pastured eggs… The “girls” (hens) roam our 6 acres eating whatever suits their fancy. We also supplement them with non-GMO feed.</p>
  </div>

  <div class="abs order-title">ORDER FORM: Please Fill Out</div>
  <div class="abs field" style="top:813px"><span>Name</span></div>
  <div class="abs field" style="top:851px"><span>Address</span></div>
  <div class="abs field" style="top:889px"><span style="width:168px">City</span><span style="width:52px">State</span><span>Zip</span></div>
  <div class="abs field" style="top:928px"><span style="width:168px">Telephone (Home)</span><span>Telephone (Cell)</span></div>
  <div class="abs field" style="top:966px"><span>Email</span></div>

  <div class="abs shares">
    <h4>Share Options (Please Check):</h4>
    <div class="sub">Summer CSA - 18 weeks<br>(Weekly delivery starting June 1st through October 11th)</div>
    <div class="check" style="margin-left:10px"><i></i><span><b>Mini Share</b> $325.00</span></div>
    <div class="check" style="margin-left:10px"><i></i><span><b>Standard Share</b> $425.00</span></div>
    <div class="check" style="margin-left:10px"><i></i><span><b>Family Share</b> $500.00</span></div>
    <div style="font-size:11px;margin:12px 0 2px 34px">ADD-ONS</div>
    <div class="check" style="margin-left:10px;margin-bottom:2px"><i></i><span><b>Fruit Share</b> <span style="font-size:7px;font-style:italic">(please select size)</span></span></div>
    <div class="check indent" style="margin-left:18px;margin-bottom:2px"><i class="sm"></i><span>Small $50</span></div>
    <div class="check indent" style="margin-left:18px;margin-bottom:4px"><i class="sm"></i><span>Large $75</span></div>
    <div class="check" style="margin-left:10px"><i></i><span><b>Egg Share</b> $90</span></div>
  </div>

  <div class="abs pref">
    <h4>Preferred Pick Up Location for Summer CSA (Please Check):</h4>
    <div class="check"><i></i><span><b>Tuesday</b> at Maple Hollow Farm</span></div>
    <div class="check"><i></i><span><b>Tuesday Afternoon</b> at Cedar Grove Community Church, Millbrook</span></div>
    <div class="check"><i></i><span><b>Saturdays</b> at Riverside Farmers Market</span></div>
    <div class="circle">Please circle: &nbsp;<b>Pre-picked</b> &nbsp;or&nbsp; <b>Market Shopper</b></div>
    <h4 style="margin-top:18px">Payment Options (Please Check):</h4>
    <div class="check"><i></i><span><b>Check</b> made payable to: Daniel Whitford/Maple Hollow Farm</span></div>
    <div class="check"><i></i><span><b>Debit/Credit Card/E-Pay</b> on website (coming soon!)</span></div>
    <div class="check"><i></i><span><b>Money Order</b> (Daniel Whitford / Maple Hollow Farm)</span></div>
  </div>

  <div class="abs terms">
    <h5>CSA MEMBER RESPONSIBILITIES - PLEASE READ</h5>
    <p>As a CSA member, you share in the bounty as well as the potential risks that may occur on the farm. Being a member enables you to form a relationship with the farmer, the farm and the people that are involved with growing the crops. Becoming a member is a commitment. We ask that if you can’t finish the season as members, then you are welcome to reassign your share to another family, but we cannot issue a refund. We also want you to be fully free to share your expectations and feedback on the produce, fruit, and eggs you receive. We will strive to give you the best we have to offer, and make sure you are satisfied with our produce.</p>
    <p><strong>If you are unable to pick up your box on delivery day, you must make alternate arrangements for your produce ahead of time.</strong></p>
    <p>You can have someone else pick up your box, ask the farm not to make your box that week, or ask your site coordinator to hold the box for a later pick-up. If you forget to pick up your share, it will be donated to a food pantry or a neighborhood family. <strong>KINDLY READ ANY EMAILS THAT WE SEND OUT TO YOU!</strong> This is how we communicate with you with announcements, recipes, events and special offers!</p>
  </div>

  <div class="abs mail">
    Please send to Completed<br>Form and Check to:<br>
    <em>Maple Hollow Farm<br>Daniel &amp; Clara Whitford<br>1280 Orchard Lane<br>Brookfield, VA 24099</em>
  </div>
</body>
</html>
```